Business Card for Jewelry Business

We need a new namecard design for a jewelry company based in Bangkok, Thailand. We have a new website recently and want the new namecard to reflect our new modern image. I have uploaded our old namecard to show you the information that needs to be on the namecard. Pls check our website www.qelburn.com for the new color scheme to help design the new namecard.

```html
<!DOCTYPE html>
<html lang="en">
<head>
<meta charset="utf-8">
<title>Qelburn Makers – Business Cards</title>
<link href="https://fonts.googleapis.com/css2?family=Cormorant+Garamond:wght@500&family=Montserrat:wght@400;500&display=swap" rel="stylesheet">
<style>
  :root {
    --teal: #52c2c7;
    --beige: #ddd5cb;
    --ink: #3d3d3d;
    --paper: #ffffff;
    --backdrop: #eceeef;
  }
  html, body {
    margin: 0;
    width: 1200px;
    height: 1200px;
    overflow: hidden;
    background: var(--backdrop);
    font-family: "Montserrat", sans-serif;
  }
  .card {
    position: absolute;
    left: 170px;
    width: 860px;
    height: 490px;
    background: var(--paper);
    overflow: hidden;
    box-shadow: 0 6px 18px rgba(0,0,0,0.12);
  }
  .card--front { top: 60px; }
  .card--back { top: 650px; }

  /* Front */
  .front-field {
    position: absolute; left: 0; top: 0; width: 100%; height: 330px;
    background: var(--teal);
  }
  .front-tab {
    position: absolute; left: 210px; top: 300px; width: 440px; height: 30px;
    background: var(--beige);
  }
  .brand-mark {
    position: absolute; left: 0; top: 120px; width: 100%;
    display: flex; justify-content: center; align-items: center; gap: 16px;
  }
  .brand-mark__dot {
    width: 34px; height: 34px; border-radius: 50%;
    border: 2px solid var(--paper);
  }
  .brand-mark__name {
    font-family: "Montserrat", sans-serif; font-weight: 500;
    font-size: 34px; letter-spacing: 6px; color: var(--paper);
  }
  .company-name {
    position: absolute; left: 210px; top: 352px;
    font-size: 24px; font-weight: 500; letter-spacing: 1.5px; color: var(--ink);
    text-transform: uppercase;
  }
  .company-web {
    position: absolute; left: 330px; top: 398px;
    display: flex; align-items: center; gap: 10px;
    font-size: 20px; font-weight: 500; color: var(--ink);
  }

  /* Back */
  .accent-rule {
    position: absolute; left: 560px; top: 90px; width: 300px; height: 14px;
    background: var(--teal);
  }
  .seal {
    position: absolute; left: 650px; top: 150px; width: 150px; height: 150px;
    border: 2px solid var(--beige); border-radius: 50%;
    display: flex; align-items: center; justify-content: center;
    font-weight: 500; font-size: 18px; letter-spacing: 3px; color: var(--teal);
  }
  .person-name {
    position: absolute; left: 60px; top: 180px; margin: 0;
    font-family: "Cormorant Garamond", serif; font-weight: 500;
    font-size: 46px; letter-spacing: 2px; color: var(--teal); text-transform: uppercase;
  }
  .person-role {
    position: absolute; left: 62px; top: 236px; margin: 0;
    font-size: 18px; line-height: 22px; letter-spacing: 1px; color: var(--ink);
    text-transform: uppercase;
  }
  .icon-column {
    position: absolute; left: 0; top: 300px; width: 180px; height: 190px;
    background: var(--teal);
  }
  .icon {
    position: absolute; left: 118px;
  }
  .contact {
    position: absolute; left: 210px; margin: 0;
    font-size: 17px; line-height: 22px; color: var(--ink);
  }
</style>
</head>
<body>

<section class="card card--front">
  <div class="front-field"></div>
  <div class="brand-mark">
    <span class="brand-mark__dot"></span>
    <span class="brand-mark__name">QELBURN</span>
  </div>
  <div class="front-tab"></div>
  <div class="company-name">Qelburn Makers Co., Ltd</div>
  <div class="company-web">
    <svg width="20" height="20" viewBox="0 0 20 20" aria-hidden="true">
      <circle cx="10" cy="10" r="8.5" fill="none" stroke="#3d3d3d" stroke-width="1.6"/>
      <ellipse cx="10" cy="10" rx="3.6" ry="8.5" fill="none" stroke="#3d3d3d" stroke-width="1.4"/>
      <line x1="1.5" y1="10" x2="18.5" y2="10" stroke="#3d3d3d" stroke-width="1.4"/>
    </svg>
    <span>www.qelburn.net</span>
  </div>
</section>

<section class="card card--back">
  <div class="accent-rule"></div>
  <div class="seal">QELBURN</div>

  <h1 class="person-name">Nira Thanakul</h1>
  <p class="person-role">Sales &amp; Product<br>Development Meneger</p>

  <div class="icon-column">
    <svg class="icon" style="top:30px" width="24" height="18" viewBox="0 0 24 18" aria-label="Email">
      <rect x="1" y="1" width="22" height="16" fill="none" stroke="#fff" stroke-width="1.6"/>
      <polyline points="1,1 12,10 23,1" fill="none" stroke="#fff" stroke-width="1.6"/>
    </svg>
    <svg class="icon" style="top:74px;left:121px" width="18" height="18" viewBox="0 0 18 18" aria-label="Social page">
      <circle cx="9" cy="9" r="7.5" fill="none" stroke="#fff" stroke-width="1.6"/>
    </svg>
    <svg class="icon" style="top:104px;left:121px" width="18" height="18" viewBox="0 0 18 18" aria-label="Social profile">
      <rect x="1.5" y="1.5" width="15" height="15" fill="none" stroke="#fff" stroke-width="1.6"/>
    </svg>
    <svg class="icon" style="top:134px;left:121px" width="18" height="24" viewBox="0 0 18 24" aria-label="Address">
      <path d="M9 22 C4 15 1.5 11 1.5 8 A7.5 7.5 0 0 1 16.5 8 C16.5 11 14 15 9 22 Z" fill="none" stroke="#fff" stroke-width="1.6"/>
      <circle cx="9" cy="8" r="2.6" fill="none" stroke="#fff" stroke-width="1.4"/>
    </svg>
  </div>

  <p class="contact" style="top:318px">nira@qelburn.com<br>hello@qelburn.com</p>
  <p class="contact" style="top:372px">Qelburn Makers</p>
  <p class="contact" style="top:402px">QelburnMkr</p>
  <p class="contact" style="top:432px;font-size:14px;line-height:17px">218 Moo 7 Rattanakosin Road,<br>Trade Processing Zone 2, Nong Bon Industrial Park,<br>Prawet, Bangkok 10250 Thailand</p>
</section>

</body>
</html>
```